Tap Tidy Pure is an under sink water filtration product for the domestic market which will replace the need to purchase bottled water in the home.

The water filter provides safe delicious drinking water at the kitchen sink.

Priced at €2.99 per week

I am looking for a series of five flyers.

Re-develope the attached one and we will get you to develop a series of five more.
Updates

To Designers

This is my first time using this service and therefore is a test with a small investment. None of the designs posted so far are up to the standard required. I do like the parachute idea but would need to be more finished. The original flyer provided with the original brief is without doubt the best by far. 
I am not sure what the next step is however I cannot use anything produced so far.

Target Market(s)

Domestic home owner.

Requirements
Must have
• See attached example
Nice to have
• See attached

```html
<!DOCTYPE html>
<html lang="en">
<head>
<meta charset="utf-8">
<title>Tap Tidy Pure – Flyer</title>
<link href="https://fonts.googleapis.com/css2?family=Archivo+Black&display=swap" rel="stylesheet">
<style>
  :root {
    --sky-top: #2a86e6;
    --sky-mid: #4fa6ee;
    --sky-low: #8fcdf3;
    --sky-foot: #e6f6fd;
    --ink-blue: #1e63db;
    --deep-blue: #0f4fc4;
    --white: #ffffff;
    --sticker-blue: #2b7fe0;
    --sticker-light: #7cc2f6;
    --scene-a: #cfe9f7;
    --scene-b: #7fc3ea;
  }
  html, body {
    margin: 0;
    padding: 0;
    overflow: hidden;
    background: #ffffff;
  }
  .flyer {
    position: relative;
    width: 857px;
    height: 1200px;
    overflow: hidden;
    background: linear-gradient(180deg, var(--sky-top) 0%, var(--sky-mid) 35%, var(--sky-low) 75%, var(--sky-foot) 100%);
    font-family: "Archivo Black", "Arial Black", sans-serif;
  }

  /* price sticker */
  .price-sticker {
    position: absolute;
    left: -30px;
    top: -40px;
    width: 270px;
    height: 270px;
  }
  .price-sticker__text {
    position: absolute;
    left: 40px;
    top: 34px;
    width: 170px;
    text-align: center;
    color: var(--white);
    transform: rotate(-14deg);
    line-height: 1;
  }
  .price-sticker__small { font-size: 22px; letter-spacing: 4px; display: block; }
  .price-sticker__amount { font-size: 40px; display: block; margin: 2px 0; }

  /* headline */
  .headline {
    position: absolute;
    left: 30px;
    top: 232px;
    margin: 0;
    font-size: 84px;
    line-height: 1;
    color: var(--white);
    letter-spacing: 3px;
    transform: rotate(-4deg);
    transform-origin: left bottom;
    text-shadow: 0 0 2px var(--deep-blue), 3px 4px 6px rgba(10, 60, 170, .75);
    white-space: nowrap;
  }
  .tagline {
    position: absolute;
    left: 30px;
    top: 318px;
    margin: 0;
    font-size: 22px;
    line-height: 1;
    color: var(--white);
    transform: rotate(-4deg);
    transform-origin: left bottom;
    text-shadow: 0 0 2px var(--deep-blue), 2px 3px 4px rgba(10, 60, 170, .8);
    white-space: nowrap;
  }

  /* product scene placeholder */
  .product-scene {
    position: absolute;
    left: 140px;
    top: 385px;
    width: 390px;
    height: 525px;
    border-radius: 18px;
    background: linear-gradient(160deg, var(--scene-a) 0%, var(--scene-b) 100%);
    opacity: .85;
  }

  /* no bottle icon */
  .no-bottle {
    position: absolute;
    left: 600px;
    top: 670px;
    width: 240px;
    height: 240px;
  }

  /* body copy */
  .body-copy {
    position: absolute;
    left: 26px;
    top: 920px;
    width: 720px;
    margin: 0;
    font-family: "Archivo Black", "Arial Black", sans-serif;
    font-size: 17px;
    line-height: 1.2;
    color: var(--ink-blue);
    text-transform: uppercase;
    text-shadow: 0 0 3px var(--white), 0 0 6px var(--white);
  }
  .body-copy p { margin: 0 0 22px; }

  /* call to action */
  .contact {
    position: absolute;
    left: 0;
    top: 1070px;
    width: 857px;
    text-align: center;
    color: var(--ink-blue);
    font-size: 40px;
    line-height: 1.65;
    text-shadow: 0 0 3px var(--white), 0 0 6px var(--white), 0 0 10px rgba(255,255,255,.8);
  }
  .contact__line { display: block; }
</style>
</head>
<body>
<main class="flyer">

  <div class="price-sticker">
    <svg width="270" height="270" viewBox="0 0 270 270" aria-hidden="true">
      <defs>
        <radialGradient id="stickerFill" cx="45%" cy="40%" r="60%">
          <stop offset="0%" stop-color="#4aa1ef"/>
          <stop offset="100%" stop-color="#1f6fd4"/>
        </radialGradient>
      </defs>
      <circle cx="135" cy="135" r="128" fill="#ffffff"/>
      <circle cx="135" cy="135" r="118" fill="url(#stickerFill)"/>
      <path d="M238 150 Q250 205 205 238 Q215 195 238 150 Z" fill="#e9f5ff" stroke="#9ccbf2" stroke-width="2"/>
    </svg>
    <div class="price-sticker__text">
      <span class="price-sticker__small">Only</span>
      <span class="price-sticker__amount">2.99</span>
      <span class="price-sticker__small">A week</span>
    </div>
  </div>

  <h1 class="headline">TAP TIDY PURE!!</h1>
  <p class="tagline">MAKING YOUR TAP WATER DELICIOUS AND SAFE TO DRINK!!</p>

  <div class="product-scene" role="img" aria-label="Person holding a glass of water beside a kitchen sink with a chrome tap"></div>

  <svg class="no-bottle" viewBox="0 0 240 240" aria-label="No bottled water icon" role="img">
    <g transform="rotate(-30 120 120)">
      <rect x="100" y="62" width="40" height="18" rx="4" fill="#ffffff" stroke="#2b7fe0" stroke-width="3"/>
      <path d="M96 80 H144 Q156 96 156 112 V176 Q156 186 146 186 H94 Q84 186 84 176 V112 Q84 96 96 80 Z"
            fill="#d6ecfb" stroke="#2b7fe0" stroke-width="3"/>
      <rect x="84" y="122" width="72" height="30" fill="#3b8ee6"/>
    </g>
    <circle cx="120" cy="120" r="100" fill="none" stroke="#ffffff" stroke-width="20"/>
    <circle cx="120" cy="120" r="111" fill="none" stroke="#2b7fe0" stroke-width="2"/>
    <circle cx="120" cy="120" r="89" fill="none" stroke="#2b7fe0" stroke-width="2"/>
    <line x1="50" y1="50" x2="190" y2="190" stroke="#ffffff" stroke-width="20"/>
  </svg>

  <section class="body-copy">
    <p>Tap Tidy Pure is an under sink water filtration product for the domestic market which will replace the need to purchase bottled water in the home.</p>
    <p>The water filter provides safe delicious drinking water at the kitchen sink.</p>
  </section>

  <div class="contact">
    <span class="contact__line">FOR MORE INFO CALL</span>
    <span class="contact__line">1(870)-555-019</span>
  </div>

</main>
</body>
</html>
```